Modernes Karten-Design für Finanzdienstleister
Zielgruppe
Wir sind ein Finanzdienstleister, der zum einen Teil auf Provisionsbasis und zum anderen Teil auf Honorarbasis arbeitet. Hierfür haben wir auch getrennte Firmenbereiche. Unser Kundenklientel sind Privatpersonen im Alter zwischen 35 und 80 Jahren. Unsere Dienstleistungen drehen sich um alle Versicherungen, aber auch um Geldanlagen, Verfügungen, Vollmachten und Testamente
Aufgabenstellung
Wir benötigen eine Karte, die wir an Kunden verschicken, wenn wir Unterlagen verschicken. Die Karte, die wir bisher haben finden Sie bei den Dateien, die wir hochgeladen haben. Wir möchten nun eine moderne Karte haben mit der wir uns bei unseren Kunden bedanken. Auf der Rückseite der Karte soll wie bisher Platz sein für einen handschriftlichen Gruß von uns oder für sonstige handschriftliche Vermerke. Beim Format der Karte sind wir fexibel. Es müssen unsere Firmenfarben und unser Slogan verwendet werden. Wir möchten ein schnörkelloses modernes Design haben. Bei den hochgeladenen Unterlagen befinden sich auch Vorschläge, die ein Mitarbeiter bereits entworfen hat. Diese gefallen uns aber nicht. Die Webadresse unserer Webseite lautet: https://lindmayr-horizonte.de/
Auf der Rückseite sollen natürlich auch die Adress- und Kontaktdaten mit drauf sein. Wir brauchen hier keine eigenen Bilder und auch kein Stockmaterial. Die Karte soll einfach, schlicht aber stylisch modern sein.

```html
<!DOCTYPE html>
<html lang="de">
<head>
<meta charset="utf-8">
<title>Danke-Karte – lindmayr horizonte</title>
<link rel="stylesheet" href="https://fonts.googleapis.com/css2?family=Poppins:wght@500;600;700&display=swap">
<style>
  :root {
    --brand-orange: #e57118;
    --ink: #231f20;
    --paper: #ffffff;
    --backdrop: #ececec;
  }
  * { margin: 0; padding: 0; box-sizing: border-box; }
  html, body { width: 1200px; height: 4356px; overflow: hidden; }
  body {
    background: var(--backdrop);
    font-family: "Poppins", sans-serif;
    position: relative;
  }
  .card {
    position: absolute;
    left: 214px;
    width: 772px;
    height: 545px;
    background: var(--paper);
  }
  .card--front { top: 213px; background: var(--brand-orange); }
  .card--back-a { top: 1022px; }
  .card--back-b { top: 1894px; }
  .card--back-c { top: 2758px; }
  .card--back-d { top: 3592px; }

  .headline {
    position: absolute;
    left: 58px; top: 50px;
    color: var(--paper);
    font-weight: 600;
    font-size: 80px;
    line-height: 1;
    letter-spacing: 0.5px;
  }
  .rule { position: absolute; height: 5px; background: var(--brand-orange); }
  .rule--light { background: var(--paper); height: 7px; }

  .brand {
    position: absolute;
    text-align: center;
    width: 340px;
  }
  .brand__name {
    display: block;
    font-weight: 500;
    font-size: 33px;
    line-height: 1.1;
    color: var(--ink);
    letter-spacing: -0.3px;
  }
  .brand__claim {
    display: block;
    font-weight: 500;
    font-size: 16px;
    color: var(--ink);
    margin-top: 4px;
  }

  .contact {
    position: absolute;
    font-weight: 600;
    font-size: 16.5px;
    line-height: 23px;
    color: var(--brand-orange);
    font-style: normal;
  }
</style>
</head>
<body>

  <section class="card card--front" aria-label="Vorderseite">
    <h1 class="headline">Danke</h1>
    <div class="rule rule--light" style="left:454px; top:449px; width:318px;"></div>
  </section>

  <section class="card card--back-a" aria-label="Rückseite, Variante 1">
    <div class="brand" style="right:50px; top:56px;">
      <span class="brand__name">lindmayr horizonte</span>
      <span class="brand__claim">Weiter vorausdenken.</span>
    </div>
    <div class="rule" style="left:0; top:381px; width:363px;"></div>
    <address class="contact" style="left:60px; top:415px;">
      Lindenweg 12 • 79098 Freiburg<br>
      Telefon : 0761/48 27 30-15<br>
      info@lindmayr-horizonte.de<br>
      www.lindmayr-horizonte.de
    </address>
  </section>

  <section class="card card--back-b" aria-label="Rückseite, Variante 2">
    <div class="brand" style="right:50px; top:56px;">
      <span class="brand__name">lindmayr horizonte</span>
      <span class="brand__claim">Weiter vorausdenken.</span>
    </div>
    <div class="rule" style="left:409px; top:381px; width:363px;"></div>
    <address class="contact" style="left:60px; top:415px;">
      Lindenweg 12 • 79098 Freiburg<br>
      Telefon : 0761/48 27 30-15<br>
      info@lindmayr-horizonte.de<br>
      www.lindmayr-horizonte.de
    </address>
  </section>

  <section class="card card--back-c" aria-label="Rückseite, Variante 3">
    <div class="rule" style="left:45px; top:381px; width:682px;"></div>
    <address class="contact" style="left:60px; top:415px;">
      Lindenweg 12 • 79098 Freiburg<br>
      Telefon : 0761/48 27 30-15<br>
      info@lindmayr-horizonte.de<br>
      www.lindmayr-horizonte.de
    </address>
    <div class="brand" style="right:50px; top:432px;">
      <span class="brand__name">lindmayr horizonte</span>
      <span class="brand__claim">Weiter vorausdenken.</span>
    </div>
  </section>

  <section class="card card--back-d" aria-label="Rückseite, Variante 4">
    <div class="brand" style="left:216px; top:56px;">
      <span class="brand__name">lindmayr horizonte</span>
      <span class="brand__claim">Weiter vorausdenken.</span>
    </div>
    <div class="rule" style="left:66px; top:418px; width:640px;"></div>
    <address class="contact" style="left:91px; top:462px;">
      Lindenweg 12 • 79098 Freiburg<br>
      Telefon : 0761/48 27 30-15
    </address>
    <address class="contact" style="left:414px; top:462px;">
      info@lindmayr-horizonte.de<br>
      www.lindmayr-horizonte.de
    </address>
  </section>

</body>
</html>
```